Sleek, Professional Business Card Design Needed

Business Cards - Logo Attached.

We are a solar consulting company. We are national and want our cards to represent the professional high quality products that we offer.

Industry/Entity Type

Business

Contact Information for Business Card

n/a

Requirements
Must have
• Design
• Name
• Position
• Number
• Email
• Address
Should not have
• Not be too crowded

```html
<!DOCTYPE html>
<html lang="en">
<head>
<meta charset="utf-8">
<title>Bright Field Solar – Business Card</title>
<link rel="stylesheet" href="https://fonts.googleapis.com/css2?family=Open+Sans:wght@400;600&display=swap">
<style>
  :root {
    --backdrop: #e9e6e1;
    --card-dark: #2f3032;
    --card-dark-ring: #37383a;
    --card-light: #ffffff;
    --ring-light: #ececec;
    --brand-blue: #2a9ad8;
    --brand-green: #8cc63f;
    --text-grey: #6f6f6f;
  }
  * { box-sizing: border-box; margin: 0; padding: 0; }
  html, body {
    width: 1200px; height: 800px; overflow: hidden;
    background: var(--backdrop);
    font-family: "Open Sans", Arial, sans-serif;
  }
  .sheet {
    width: 1200px; height: 800px;
    display: flex; align-items: center; justify-content: center; gap: 40px;
  }
  .card {
    position: relative; width: 540px; height: 310px;
    border-radius: 18px; overflow: hidden;
    box-shadow: 0 10px 28px rgba(0,0,0,.18);
  }
  .card--front { background: var(--card-dark); }
  .card--back { background: var(--card-light); }

  .deco-ring {
    position: absolute; border-radius: 50%;
    border-style: solid;
  }
  .card--front .deco-ring {
    width: 300px; height: 300px; left: 120px; top: 5px;
    border-width: 26px; border-color: var(--card-dark-ring);
  }
  .card--back .deco-ring {
    width: 240px; height: 240px; right: 60px; top: 40px;
    border-width: 18px; border-color: var(--ring-light);
  }

  .brand { position: absolute; display: flex; flex-direction: column; align-items: center; }
  .brand__mark { border-radius: 50%; background: var(--brand-blue); }
  .brand__name {
    color: var(--brand-blue); font-weight: 600; letter-spacing: 2px;
    text-transform: uppercase; white-space: nowrap;
  }
  .brand__rule { height: 2px; background: var(--brand-green); }

  .card--front .brand { left: 0; right: 0; top: 70px; }
  .card--front .brand__mark { width: 56px; height: 56px; margin-bottom: 14px; }
  .card--front .brand__name { font-size: 30px; }
  .card--front .brand__rule { width: 300px; margin-top: 8px; }
  .card--front .website {
    position: absolute; left: 0; right: 0; top: 222px; text-align: center;
    color: var(--brand-green); font-size: 14px;
  }

  .card--back .brand { right: 34px; top: 34px; align-items: flex-end; }
  .card--back .brand__mark { width: 34px; height: 34px; margin-bottom: 8px; }
  .card--back .brand__name { font-size: 18px; }
  .card--back .brand__rule { width: 190px; margin-top: 5px; }
  .card--back .website {
    position: absolute; right: 34px; top: 132px;
    color: var(--brand-green); font-size: 13px;
  }

  .person {
    position: absolute; left: 34px; top: 48px;
    border-left: 5px solid var(--brand-blue); padding-left: 12px;
  }
  .person__name { color: var(--text-grey); font-size: 22px; line-height: 1.15; }
  .person__title { color: var(--brand-green); font-size: 13px; }

  .contact { position: absolute; left: 34px; bottom: 30px; list-style: none; }
  .contact li {
    display: flex; align-items: center; gap: 10px;
    color: var(--text-grey); font-size: 13px; margin-top: 8px;
  }
  .contact svg { width: 16px; height: 16px; fill: var(--brand-blue); }
</style>
</head>
<body>
<main class="sheet">
  <section class="card card--front" aria-label="Card front">
    <div class="deco-ring"></div>
    <div class="brand">
      <span class="brand__mark"></span>
      <span class="brand__name">Bright Field Solar</span>
      <span class="brand__rule"></span>
    </div>
    <p class="website">yourwebsite.com</p>
  </section>

  <section class="card card--back" aria-label="Card back">
    <div class="deco-ring"></div>
    <div class="brand">
      <span class="brand__mark"></span>
      <span class="brand__name">Bright Field Solar</span>
      <span class="brand__rule"></span>
    </div>
    <p class="website">yourwebsite.com</p>

    <div class="person">
      <p class="person__name">Your Name</p>
      <p class="person__title">Job Title</p>
    </div>

    <ul class="contact">
      <li>
        <svg viewBox="0 0 24 24" aria-hidden="true"><path d="M6.6 10.8a15 15 0 0 0 6.6 6.6l2.2-2.2c.3-.3.7-.4 1-.2 1.1.4 2.3.6 3.6.6.6 0 1 .4 1 1V20c0 .6-.4 1-1 1C10.6 21 3 13.4 3 4c0-.6.4-1 1-1h3.5c.6 0 1 .4 1 1 0 1.3.2 2.5.6 3.6.1.3 0 .7-.2 1z"/></svg>
        <span>000 000 0000</span>
      </li>
      <li>
        <svg viewBox="0 0 24 24" aria-hidden="true"><path d="M3 5h18c.6 0 1 .4 1 1v12c0 .6-.4 1-1 1H3c-.6 0-1-.4-1-1V6c0-.6.4-1 1-1zm9 7.2L20 7H4z"/></svg>
        <span>youremail@xyz.com</span>
      </li>
    </ul>
  </section>
</main>
</body>
</html>
```